Ebook Cover Design for Coif PaNORAma!

I wrote a three-part series based on my year in beauty school as a more mature student (34yo as opposed to the mostly 20yo crowd). It's called Coif PaNORAma, based on the blog of the same name that I kept the entire year. While there, I won many competitions, I was on student council, my mom passed away from cancer, and I traveled to Washington, D.C., to speak to Senate Hall about colon cancer research and prevention (for my mom). It's got a bit of everything. The book is considered a work of narrative nonfiction or creative nonfiction. Basically, it's a memoir.

The three titles are:

Coif PaNORAma: Frayed Tips
Coif PaNORAma: Lather Once More
Coif PaNORAma: A Quiet Braid

So, three book covers altogether. Different colors but same theme.

(My name is NORA, hence the clever title. Heh.)

Am willing to consider not using a colon after "PaNORAma."

Also, the way it's spelled...Coif PaNORAma...it's important to keep that capitalization because of my name in the word "PaNORAma."

My pseudonym is Nora Bellwyn. That should, of course, be included on the cover.

The cover should meet the specs required for uploading to Quillmart and Pagevault.

Thanks for your ideas! x
Updates

I want to make it clear I am looking for the first cover only at this point for Coif PaNORAma: Frayed Tips (Frayed Tips is the subtitle).My author name is Nora Bellwyn. Very important! Added Saturday, October 11, 2014

Project Deadline Extended Reason: I have been busy volunteering for a political campaign while also doing my day job. I appreciate the submissions thus far! x Added Sunday, October 19, 2014

Project Deadline Extended Reason: I was involved with a political campaign that took up a lot of my time unexpectedly in the end. Extending deadline for this reason! x Added Tuesday, November 11, 2014

Target Market(s)

Teen to adult women. It reads like chick lit.

Industry/Entity Type

School

Font styles to use
Decorative

Requirements
Must have
• My name "Nora" must stand out somehow in the word "PaNORAma."
Nice to have
• Cosmetology related items, like blow dryer, shears (hair cutting scissors), combs, etc.
Should not have
• No red, white and blue themes. No blue cancer ribbons. Just hair-related items.

```html
<!DOCTYPE html>
<html lang="en">
<head>
<meta charset="utf-8">
<title>Coif PaNORAma: Frayed Tips — Nora Bellwyn</title>
<link rel="stylesheet" href="https://fonts.googleapis.com/css2?family=Cinzel:wght@600;700&family=Cormorant+Garamond:wght@500&display=swap">
<style>
  :root {
    --cover-white: #ffffff;
    --cover-lilac: #ece4f2;
    --cover-lavender: #b9a2cd;
    --cover-violet: #8a68a8;
    --series-purple: #5a2a86;
    --title-ink: #151515;
    --rule-grey: #b8afc0;
    --steel-light: #e6e6ea;
    --steel-dark: #8d8d96;
  }
  html, body {
    margin: 0;
    padding: 0;
    width: 800px;
    height: 1200px;
    overflow: hidden;
  }
  .cover {
    position: relative;
    width: 800px;
    height: 1200px;
    overflow: hidden;
    background:
      radial-gradient(ellipse 70% 58% at 50% 48%, var(--cover-white) 0%, var(--cover-white) 45%, var(--cover-lilac) 68%, var(--cover-lavender) 88%, var(--cover-violet) 110%);
  }
  .series-title {
    position: absolute;
    top: 52px;
    left: 0;
    width: 100%;
    margin: 0;
    text-align: center;
    font-family: "Cinzel", serif;
    font-weight: 700;
    font-size: 64px;
    line-height: 1;
    letter-spacing: 1px;
    color: var(--series-purple);
  }
  .series-rule {
    position: absolute;
    top: 146px;
    left: 190px;
    width: 420px;
    height: 2px;
    background: linear-gradient(90deg, transparent, var(--rule-grey) 15%, var(--rule-grey) 85%, transparent);
  }
  .series-dots {
    position: absolute;
    top: 158px;
    left: 0;
    width: 100%;
    display: flex;
    justify-content: center;
    gap: 8px;
  }
  .series-dots span {
    width: 6px;
    height: 6px;
    border-radius: 50%;
    background: var(--rule-grey);
  }
  .book-title {
    position: absolute;
    top: 200px;
    left: 0;
    width: 100%;
    margin: 0;
    text-align: center;
    font-family: "Cormorant Garamond", serif;
    font-weight: 500;
    font-size: 200px;
    line-height: 0.96;
    color: var(--title-ink);
  }
  .book-title span { display: block; }
  .shears-art {
    position: absolute;
    top: 690px;
    left: 200px;
    width: 430px;
    height: 260px;
    border-radius: 50% 40% 45% 55% / 55% 45% 55% 45%;
    background: radial-gradient(ellipse at 45% 45%, var(--steel-light) 0%, #c9c9d0 55%, rgba(141,141,150,0.35) 80%, transparent 100%);
    transform: rotate(-18deg);
  }
  .author-name {
    position: absolute;
    bottom: 44px;
    left: 0;
    width: 100%;
    margin: 0;
    text-align: center;
    font-family: "Cinzel", serif;
    font-weight: 600;
    font-size: 36px;
    letter-spacing: 2px;
    color: var(--series-purple);
  }
</style>
</head>
<body>
  <main class="cover">
    <h2 class="series-title">Coif PaNORAma</h2>
    <div class="series-rule"></div>
    <div class="series-dots"><span></span><span></span><span></span></div>
    <h1 class="book-title"><span>Frayed</span><span>Tips</span></h1>
    <div class="shears-art" role="img" aria-label="Silver hair-cutting shears with a curling strand of dark hair"></div>
    <p class="author-name">NORA BELLWYN</p>
  </main>
</body>
</html>
```